Wordpress Powered Website. Outstanding Design Required. Using Morvento Theme

Designers will not need to create anything other than the home page but there are some design elements on the home page which also need to be factored in: 6 product place holders and 2-3 slides for a slideshow (with images I provide).

Designers will need to familiarise themselves with the Morvento theme to make sure that their design will work within the theme.

The winning designer will set up all the pages and navigation in place. This includes social media icons, favicon, widgets, etc. In other words, the home page needs to be designed and coded and the other preset theme pages need to be organised in a way that we can start using the website on completion of the job.

Most of the designs I had last time were too colourful. This needs to be subtle not in your face.

Background to the business/website:
Tallow Banners is a new Australian venture which will sell large format printed banners and other signage. The market is very competitive so it is important to stand out visually and to have a website which is clean, easy to navigate and easy to order. It will be a combination of online sales and assisted sales but all sales enquiries will come from the website.

As our business is focused on presentation it is vital to have excellent design.
Purchased theme is Morvento. Only this theme is to be used.

1. A home page using all the preset features of the Morvento theme - it will just be basically taking my wireframe and inputting it to the live theme.
2. A three slide slideshow, ideally with an edited video. The static image slides can be provided by me during the handover. Placeholder for now.
Similar to this one: http://thebrindlework.com.au/

Attached is the logo which must be utilised, although it could also sit on a dark background. There is our mascot as well which can be used but does not have to be included.

Target Market(s)

Primarily B2B (business to business)
Main industries will be Construction, Retail, Community, Events & Trade Shows

Industry/Entity Type

Printing

Coding

Coded - Design and coding required

Font styles to use
Sans Serif

Requirements
Must have
• Must have the design files made to web pages within the Wordpress environment.
Nice to have
• Clean design. Stand out from competitors based on design.
Should not have
• Should not look like any competitor

```html
<!DOCTYPE html>
<html lang="en">
<head>
<meta charset="utf-8">
<title>Tallow Banners</title>
<link href="https://fonts.googleapis.com/css2?family=Michroma&family=Open+Sans:wght@400;600;700&display=swap" rel="stylesheet">
<style>
:root{
  --orange:#f26522;
  --orange-light:#f7863b;
  --orange-dark:#e2531a;
  --yellow:#ffd21f;
  --dark:#2f2f2f;
  --footer:#252525;
  --text:#444;
  --muted:#666;
  --panel:#f3f3f3;
  --line:#d9d9d9;
  --icon:#6b6b6b;
}
*{margin:0;padding:0;box-sizing:border-box}
html,body{width:1200px;height:2880px;overflow:hidden}
body{font-family:"Open Sans",Arial,sans-serif;color:var(--text);background:#fff;position:relative}
.abs{position:absolute}
.display{font-family:"Michroma","Open Sans",sans-serif}

/* header */
.site-header{position:absolute;left:0;top:0;width:1200px;height:115px;background:#fff}
.brand{position:absolute;left:48px;top:34px;display:flex;align-items:center;gap:12px}
.brand-mark{width:40px;height:40px;background:var(--orange)}
.brand-name{font-family:"Michroma",sans-serif;font-size:30px;color:var(--orange);letter-spacing:1px}
.contact{position:absolute;top:38px;display:flex;gap:12px;align-items:flex-start;font-size:14px;color:#555;line-height:18px;text-transform:uppercase}
.contact svg{width:26px;height:30px;flex:none}

.main-nav{position:absolute;left:0;top:115px;width:1200px;height:42px;background:var(--dark);display:flex}
.main-nav a{color:#fff;text-decoration:none;font-size:13px;font-weight:600;line-height:42px;text-transform:uppercase;position:absolute;text-align:center}
.main-nav .active{background:#e8391c;width:96px;left:48px}

/* hero */
.hero{position:absolute;left:0;top:157px;width:1200px;height:435px;background:linear-gradient(180deg,var(--orange-light),var(--orange) 70%,var(--orange-dark))}
.hero-title{position:absolute;left:69px;top:70px;font-family:"Michroma",sans-serif;color:#fff;font-size:30px;line-height:35px;text-transform:uppercase}
.hero-title .hl{color:var(--yellow)}
.hero-title .b{font-weight:700}
.hero-list{position:absolute;left:69px;top:186px;list-style:none;color:#fff;font-size:15px;line-height:27px}
.hero-list li::before{content:"✓";color:#c8102e;font-weight:700;margin-right:6px}
.btn-order{position:absolute;left:81px;top:337px;width:130px;height:44px;border:2px solid #fff;border-radius:8px;color:#fff;font-size:17px;text-align:center;line-height:40px}
.hero-art{position:absolute;left:557px;top:54px;width:595px;height:346px;border-radius:40px;background:radial-gradient(ellipse at 60% 55%,#3a3a48 0%,#8a4a8f 30%,rgba(242,101,34,0) 70%)}

/* why */
.why-title{position:absolute;left:66px;top:658px;font-family:"Michroma",sans-serif;font-size:19px;color:#333;letter-spacing:1px}
.why-copy{position:absolute;left:63px;top:702px;width:455px;font-size:12.6px;line-height:21px;color:#555}
.why-copy .lead{color:#e8391c}
.feature{position:absolute;left:588px;width:560px}
.feature .ic{position:absolute;left:0;top:0;width:66px;height:66px;border-radius:50%;background:var(--icon)}
.feature h3{position:absolute;left:90px;top:0;font-family:"Michroma",sans-serif;font-size:16px;color:#333;letter-spacing:1px}
.feature p{position:absolute;left:90px;top:24px;width:430px;font-size:12.6px;line-height:21px;color:#555}

/* hot */
.hot{position:absolute;left:0;top:1137px;width:1200px;height:326px;background:var(--orange)}
.hot h2{position:absolute;left:63px;top:16px;font-size:18px;font-weight:700;color:#fff;text-transform:uppercase}
.hot-card{position:absolute;top:53px;width:242px}
.hot-card .frame{width:242px;height:134px;background:#e9e9e9;padding:10px}
.hot-card h4{margin-top:17px;font-size:15px;font-weight:700;color:#fff}
.hot-card small{display:block;font-size:12px;color:#fff;margin-top:4px}
.photo{width:100%;height:100%}

/* banners grid */
.grid-title{position:absolute;left:72px;top:1506px;font-family:"Michroma",sans-serif;font-size:24px;font-weight:700;color:#222;letter-spacing:1px}
.card{position:absolute;width:240px;height:212px;border:1px solid var(--line);border-radius:6px;background:#fff;padding:10px 10px 0}
.card .photo{height:164px}
.card h4{text-align:center;font-size:16px;font-weight:700;color:#333;margin-top:10px}

/* tabs */
.tabs{position:absolute;left:0;top:2118px;width:1200px;height:42px;border-bottom:3px solid var(--orange)}
.tab{position:absolute;top:0;height:39px;line-height:39px;font-size:14px;font-weight:600;color:#333;text-transform:uppercase;text-align:center}
.tab.on{background:var(--orange);color:#fff}
.tabs svg{position:absolute;left:594px;top:39px}
.panel{position:absolute;left:0;top:2161px;width:1200px;height:469px;background:var(--panel)}
.divider{position:absolute;left:572px;top:70px;width:1px;height:362px;background:#cfcfcf}
.perk{position:absolute;width:420px}
.perk h3{display:flex;align-items:center;gap:10px;font-size:17px;font-weight:600;color:#333;height:38px}
.perk p{font-size:13px;line-height:21px;color:#444;margin-top:2px}
.perk svg{width:38px;height:38px;flex:none}

/* footer */
.site-footer{position:absolute;left:0;top:2630px;width:1200px;height:208px;background:var(--footer);color:#fff}
.fcol{position:absolute;top:34px}
.fcol h5{font-size:14px;font-weight:700;text-transform:uppercase;margin-bottom:12px}
.fcol li{list-style:none;font-size:13px;line-height:25px;padding-left:10px;position:relative}
.fcol li::before{content:"»";position:absolute;left:-4px}
.social{position:absolute;top:83px;width:50px;height:50px;background:#4a4a4a}
.copyright{position:absolute;left:0;top:2838px;width:1200px;height:42px;background:#e8391c;color:#fff;text-align:center;font-size:12px;line-height:42px}
</style>
</head>
<body>

<header class="site-header">
  <div class="brand"><span class="brand-mark"></span><span class="brand-name">Tallow Banners</span></div>
  <div class="contact" style="left:600px">
    <svg viewBox="0 0 26 30"><path d="M3 14 13 5l10 9v13H3z" fill="#555"/><rect x="10" y="19" width="6" height="8" fill="#fff"/></svg>
    <div>Visit us<br>Ardley QT218</div>
  </div>
  <div class="contact" style="left:812px">
    <svg viewBox="0 0 26 30"><rect x="7" y="3" width="12" height="24" rx="2" fill="none" stroke="#555" stroke-width="2"/><circle cx="13" cy="23" r="1.5" fill="#555"/></svg>
    <div>Call us<br>402-555-0137</div>
  </div>
  <div class="contact" style="left:982px">
    <svg viewBox="0 0 26 30"><circle cx="13" cy="16" r="10" fill="none" stroke="#555" stroke-width="2"/><path d="M13 10v6l4 3" stroke="#555" stroke-width="2" fill="none"/></svg>
    <div>Tech support<br>help@tallowmail.com</div>
  </div>
</header>

<nav class="main-nav">
  <a class="active">Home</a>
  <a style="left:180px;width:80px">Banners</a>
  <a style="left:300px;width:70px">Flags</a>
  <a style="left:410px;width:130px">Banners Stands</a>
  <a style="left:580px;width:70px">Signs</a>
  <a style="left:690px;width:110px">Contact Us</a>
  <a style="left:830px;width:100px">About Us</a>
  <a style="left:960px;width:70px">FAQs</a>
</nav>

<section class="hero">
  <h1 class="hero-title"><span class="hl">Over 95%</span><br>Customers recommend<br><span class="b">us to their friends</span></h1>
  <ul class="hero-list">
    <li>Super Fast Turn Around</li>
    <li>No Set-up Fees</li>
    <li>Lowest Price Guaranteed</li>
    <li>Over 95% Customer Satisfaction</li>
  </ul>
  <div class="btn-order">Start Order</div>
  <div class="hero-art" role="img" aria-label="Illustration of a tablet with pens, brushes and colourful paint splashes"></div>
</section>

<section>
  <h2 class="why-title">WHY CHOOSE TALLOW BANNER?</h2>
  <div class="why-copy">
    <div class="lead">Welcome to Tallow Banner.com.au</div>
    Bannerhive is your one-stop solution for all your signage needs. We'll help you say it right in many different formats. For Banners and Signs to advertise your new business, promote your products, celebrate your Birthdays and Anniversaries - Bannerhive offers a variety of banners and signs, both pre-printed and custom designed.<br>
    Our Banners are constructed of durable vinyl and printed with the latest technology in commercial printers. We provide a wide range of banner sizes - up to 100 feet long - with the best prices anywhere.<br>
    Our vinyl signs are made of heavy hi-tech perforated vinyl film for use on storefronts, interior glass walls, mirrors - any smooth surface you choose. Design your own Vinyl Banners and Signs with our user friendly Banner Design Tool. If your artwork is camera-ready you can simply upload it. Don't know exactly what your want? Talk to our professional design team and they will design your banner FREE, at no cost to you!<br>
    At Bannerhive we always stand behind our products,
  </div>

  <div class="feature" style="top:682px">
    <div class="ic"><svg viewBox="0 0 66 66" width="66" height="66"><path d="M28 20h10l-2 14h-6z" fill="#fff"/><rect x="29" y="36" width="8" height="12" fill="#fff"/></svg></div>
    <h3>FREE DESIGN SERVICE</h3>
    <p>Our vinyl banners price includes free basic design. Our excellent graphic designers can put your dreams into reality.</p>
  </div>
  <div class="feature" style="top:787px">
    <div class="ic"><svg viewBox="0 0 66 66" width="66" height="66"><rect x="24" y="18" width="18" height="26" rx="2" fill="none" stroke="#fff" stroke-width="2"/><circle cx="33" cy="30" r="5" fill="#fff"/><path d="M29 44v6l4-2 4 2v-6" fill="#fff"/></svg></div>
    <h3>PRICE GUARANTEE</h3>
    <p>Our vinyl banners price includes free basic design. Our excellent graphic designers can put your dreams into reality.</p>
  </div>
  <div class="feature" style="top:887px">
    <div class="ic"><svg viewBox="0 0 66 66" width="66" height="66"><rect x="16" y="24" width="22" height="16" fill="#fff"/><path d="M38 28h7l5 6v6H38z" fill="#fff"/><circle cx="23" cy="42" r="3" fill="#fff"/><circle cx="44" cy="42" r="3" fill="#fff"/></svg></div>
    <h3>ENSURE QUALITY</h3>
    <p>Our vinyl banners price includes free basic design. Our excellent graphic designers can put your dreams into reality.</p>
  </div>
  <div class="feature" style="top:989px">
    <div class="ic"><svg viewBox="0 0 66 66" width="66" height="66"><circle cx="33" cy="31" r="12" fill="none" stroke="#fff" stroke-width="2"/><text x="33" y="36" text-anchor="middle" font-size="14" font-family="Open Sans,sans-serif" fill="#fff">$</text><rect x="18" y="42" width="30" height="6" fill="#fff"/></svg></div>
    <h3>FAST DELIVERY</h3>
    <p>Our vinyl banners price includes free basic design. Our excellent graphic designers can put your dreams into reality.</p>
  </div>
</section>

<section class="hot">
  <h2>Hot Vinyl Banners</h2>
  <div class="hot-card" style="left:60px"><div class="frame"><div class="photo" role="img" aria-label="Photo of an indoor restaurant promotion banner" style="background:linear-gradient(135deg,#d8d8d8,#c0392b 60%,#f5f5f5)"></div></div><h4>Cloth / Fabric Banners</h4><small>600mm x 1200mm Starts at $42.55</small></div>
  <div class="hot-card" style="left:329px"><div class="frame"><div class="photo" role="img" aria-label="Photo of a roadside health clinic billboard" style="background:linear-gradient(180deg,#6fa0d8,#c8102e 45%,#6c8a3a)"></div></div><h4>Cloth / Fabric Banners</h4><small>600mm x 1200mm Starts at $42.55</small></div>
  <div class="hot-card" style="left:607px"><div class="frame"><div class="photo" role="img" aria-label="Photo of a tall red billboard against blue sky" style="background:linear-gradient(180deg,#3f6fc8,#b81e1e 55%,#5d88d6)"></div></div><h4>Cloth / Fabric Banners</h4><small>600mm x 1200mm Starts at $42.55</small></div>
  <div class="hot-card" style="left:886px"><div class="frame"><div class="photo" role="img" aria-label="Photo of a billboard in a green field" style="background:linear-gradient(180deg,#8fb1e3,#b3b7c9 45%,#6a9a3e)"></div></div><h4>Cloth / Fabric Banners</h4><small>600mm x 1200mm Starts at $42.55</small></div>
</section>

<section>
  <h2 class="grid-title">BANNERS</h2>
  <div class="card" style="left:71px;top:1559px"><div class="photo" role="img" aria-label="Photo of a building wrap banner" style="background:linear-gradient(160deg,#2f4f7a,#d8b24a 55%,#e8e8e8)"></div><h4>Cloth / Fabric Banners</h4></div>
  <div class="card" style="left:338px;top:1559px"><div class="photo" role="img" aria-label="Photo of a lit billboard at night" style="background:linear-gradient(180deg,#1a1a1a,#8fa47d 45%,#5a2020)"></div><h4>Cloth / Fabric Banners</h4></div>
  <div class="card" style="left:616px;top:1559px"><div class="photo" role="img" aria-label="Photo of a tall red billboard against blue sky" style="background:linear-gradient(180deg,#3f6fc8,#b81e1e 55%,#5d88d6)"></div><h4>Cloth / Fabric Banners</h4></div>
  <div class="card" style="left:895px;top:1559px"><div class="photo" role="img" aria-label="Photo of a roadside store billboard" style="background:linear-gradient(180deg,#c8d8ea,#c8102e 45%,#7a8a5a)"></div><h4>Cloth / Fabric Banners</h4></div>
  <div class="card" style="left:71px;top:1799px"><div class="photo" role="img" aria-label="Photo of an indoor restaurant promotion banner" style="background:linear-gradient(135deg,#d8d8d8,#c0392b 60%,#f5f5f5)"></div><h4>Cloth / Fabric Banners</h4></div>
  <div class="card" style="left:338px;top:1799px"><div class="photo" role="img" aria-label="Photo of a roadside health clinic billboard" style="background:linear-gradient(180deg,#6fa0d8,#c8102e 45%,#6c8a3a)"></div><h4>Cloth / Fabric Banners</h4></div>
  <div class="card" style="left:616px;top:1799px"><div class="photo" role="img" aria-label="Photo of a tall red billboard against blue sky" style="background:linear-gradient(180deg,#3f6fc8,#b81e1e 55%,#5d88d6)"></div><h4>Cloth / Fabric Banners</h4></div>
  <div class="card" style="left:895px;top:1799px"><div class="photo" role="img" aria-label="Photo of a billboard in a green field" style="background:linear-gradient(180deg,#8fb1e3,#b3b7c9 45%,#6a9a3e)"></div><h4>Cloth / Fabric Banners</h4></div>
</section>

<div class="tabs">
  <div class="tab" style="left:370px;width:100px">Popular</div>
  <div class="tab on" style="left:520px;width:160px">New Arrivals</div>
  <div class="tab" style="left:730px;width:130px">Best Sellers</div>
  <svg width="12" height="8" viewBox="0 0 12 8"><path d="M0 0h12L6 7z" fill="#f26522"/></svg>
</div>

<section class="panel">
  <div class="divider"></div>
  <div class="perk" style="left:81px;top:64px">
    <h3><svg viewBox="0 0 38 38"><path d="M19 3 33 8v10c0 9-6 15-14 18C11 33 5 27 5 18V8z" fill="none" stroke="#f26522" stroke-width="3"/><path d="M12 19l5 5 9-10" fill="none" stroke="#f26522" stroke-width="3"/></svg>100% Quality Guarantee</h3>
    <p>We stand behind everything we sell by offering hassle-free returns and reshipping. In the unlikely event, if we made a mistake on your order, we will quickly send you a reprint or full refund including shipping. With thousands of reviews online, we are proud to have earned over 96 percent satisfied customers.</p>
  </div>
  <div class="perk" style="left:672px;top:72px">
    <h3><svg viewBox="0 0 38 38"><circle cx="19" cy="19" r="14" fill="none" stroke="#f26522" stroke-width="3"/><text x="19" y="26" text-anchor="middle" font-size="19" font-weight="700" font-family="Open Sans,sans-serif" fill="#f26522">$</text></svg>Best Price Guarantee</h3>
    <p>We stand behind everything we sell by offering hassle-free returns and reshipping. In the unlikely event, if we made a mistake on your order, we will quickly send you a reprint or full refund including shipping. With thousands of reviews online, we are proud to have earned over 96 percent satisfied customers.</p>
  </div>
  <div class="perk" style="left:81px;top:256px">
    <h3><svg viewBox="0 0 38 38"><rect x="2" y="10" width="22" height="16" fill="#f26522"/><path d="M24 14h7l5 6v6H24z" fill="#f26522"/><circle cx="9" cy="28" r="4" fill="#fff" stroke="#f26522" stroke-width="2"/><circle cx="29" cy="28" r="4" fill="#fff" stroke="#f26522" stroke-width="2"/></svg>Free Shipping</h3>
    <p>We stand behind everything we sell by offering hassle-free returns and reshipping. In the unlikely event, if we made a mistake on your order, we will quickly send you a reprint or full refund including shipping. With thousands of reviews online, we are proud to have earned over 96 percent satisfied customers.</p>
  </div>
  <div class="perk" style="left:672px;top:264px">
    <h3><svg viewBox="0 0 38 38"><rect x="3" y="7" width="32" height="24" fill="#f26522"/><path d="M15 14l8 6-3 1 2 4-2 1-2-4-3 2z" fill="#fff"/></svg>Free Design Proofs</h3>
    <p>We stand behind everything we sell by offering hassle-free returns and reshipping. In the unlikely event, if we made a mistake on your order, we will quickly send you a reprint or full refund including shipping. With thousands of reviews online, we are proud to have earned over 96 percent satisfied customers.</p>
  </div>
</section>

<footer class="site-footer">
  <div class="fcol" style="left:98px"><h5>Main Menu</h5><ul><li>About us</li><li>Sitemap</li><li>Customer Reviews</li><li>Special Offers</li></ul></div>
  <div class="fcol" style="left:301px"><h5>Extras</h5><ul><li>Best Price Guarantee</li><li>Free Design Proofs</li><li>100% Quality Guarantee</li><li>Contact us</li></ul></div>
  <div class="fcol" style="left:536px"><h5>Information</h5><ul><li>Privacy Policy</li><li>Contacts</li><li>Terms &amp; Conditions</li></ul></div>
  <div class="fcol" style="left:720px"><h5>Your Account</h5><ul><li>Shipping</li><li>Free Shipping</li><li>Quick Order</li><li>Instant Quote</li></ul></div>
  <div class="fcol" style="left:933px"><h5>Follow us on</h5></div>
  <div class="social" style="left:939px"></div>
  <div class="social" style="left:997px"></div>
  <div class="social" style="left:1055px"></div>
</footer>
<div class="copyright">Copyright © 2016 Tallow Banners. All Rights Reserved</div>

</body>
</html>
```